Album Jacket for young indie musicians in AFRICA #2 Baraka, Tumaini And Neema (Peace, Love And Unity)

We are ZEBO SOUND (zebo-sound.example), a music label for young African musicians living in a slum. I would like to ask you to design our new album's cover jacket. The title is Baraka, Tumaini And Neema (it means "Peace, Love And Unity" in Swahili. I entrust you whether you use English words in the design or not.), musician name is Daniel Okwaro. Add our label logo (we have various versions and can provide). I attached Daniel Okwaro's photo also. Please listen to the music of the album on Soundcloud. https://audiovault.example/tags/danielokwaro

Target Market(s)

International. not only African music funs.

Requirements
Must have
• Title, Musician's name, ZEBO SOUND Logo
• In order to upload to iTunes, I require the final that the following conditions are met.
• 1400 x 1400 pixels
• JPG file type
• 72 - 300dpi (300dpi is the best)
• Less than 25mb
• RGB color scheme (not CMYK)
Nice to have
• His music is something bright and little funny. Please express the tone of music in the design.
Should not have
• African traditional image

```html
<!DOCTYPE html>
<html lang="en">
<head>
<meta charset="utf-8">
<title>Daniel Okwaro – Baraka, Tumaini &amp; Neema</title>
<link rel="stylesheet" href="https://fonts.googleapis.com/css2?family=Open+Sans:wght@300;800&display=swap">
<style>
  :root {
    --paper: #ffffff;
    --ink: #111111;
    --title-green: #17620c;
    --shirt-red: #c0302c;
    --head-dark: #2c2a52;
    --head-teal: #2e6650;
  }
  html, body {
    margin: 0;
    padding: 0;
    overflow: hidden;
    background: var(--paper);
  }
  .album-cover {
    position: relative;
    width: 1200px;
    height: 1200px;
    overflow: hidden;
    background: var(--paper);
    font-family: "Open Sans", "Segoe UI", sans-serif;
  }
  .portrait {
    position: absolute;
    inset: 0;
    width: 1200px;
    height: 1200px;
  }
  .artist-name {
    position: absolute;
    left: 32px;
    top: 148px;
    margin: 0;
    font-weight: 300;
    font-size: 92px;
    line-height: 1;
    letter-spacing: -1px;
    color: var(--ink);
    white-space: nowrap;
  }
  .album-title {
    position: absolute;
    left: 0;
    top: 318px;
    width: 630px;
    margin: 0;
    font-weight: 300;
    color: var(--title-green);
    text-align: center;
  }
  .album-title span {
    display: block;
    font-size: 150px;
    line-height: 180px;
    letter-spacing: -2px;
  }
  .album-title .ampersand {
    font-size: 140px;
  }
  .label-mark {
    position: absolute;
    left: 46px;
    top: 1104px;
    display: flex;
    align-items: center;
    gap: 16px;
  }
  .label-dot {
    width: 46px;
    height: 46px;
    border-radius: 50%;
    background: var(--ink);
  }
  .label-name {
    font-weight: 800;
    font-size: 50px;
    line-height: 1;
    color: var(--ink);
    letter-spacing: -1px;
  }
</style>
</head>
<body>
  <main class="album-cover">
    <svg class="portrait" viewBox="0 0 1200 1200" role="img" aria-label="Portrait of the musician Daniel Okwaro in a red floral shirt, rendered in swirling marbled colours">
      <defs>
        <linearGradient id="portraitTone" x1="0" y1="0" x2="0" y2="1">
          <stop offset="0" stop-color="var(--head-dark)"/>
          <stop offset="0.22" stop-color="var(--head-teal)"/>
          <stop offset="0.5" stop-color="#25301f"/>
          <stop offset="0.6" stop-color="var(--shirt-red)"/>
          <stop offset="1" stop-color="#c8443c"/>
        </linearGradient>
      </defs>
      <path fill="url(#portraitTone)" d="M980 25 C860 30 740 110 725 240 L735 420 C745 520 790 590 830 630 L810 700 C740 760 660 800 600 860 L540 1200 L1200 1200 L1200 560 C1180 540 1150 520 1130 520 L1150 420 C1175 380 1170 290 1140 275 C1130 180 1090 60 980 25 Z"/>
    </svg>

    <h2 class="artist-name">DANIEL OKWARO</h2>

    <h1 class="album-title">
      <span>BARAKA</span>
      <span>TUMAINI</span>
      <span class="ampersand">&amp;</span>
      <span>NEEMA</span>
    </h1>

    <div class="label-mark">
      <div class="label-dot"></div>
      <div class="label-name">ZEBO SOUND</div>
    </div>
  </main>
</body>
</html>
```